3 Holiday typography sets (10x19)

I have 6 phrases that I need designed as 3 coordinated sets on a 10x19 canvas size. The 2 phrases in each set should coordinate, but each of the 3 sets can have their own look.

Set #1 - southern/casual feel
Merry Christmas to y’all and to y’all a goodnight
Christmas feels warmer in the South

Set #2 - traditional/classic feel
There’s snowplace like home (snowflakes/snowman)
Hearts come home for Christmas

Set #3 - fun/whimsical feel
Christmas calories don’t count (cookies)
He sees you when you’re eating

The accent element ideas in parentheses are optional and I am open to other design/accent elements. All 3 sets need to be on a white background.

Target Market(s)

women 25-55

Colors
ec1f27
9bcb3c
cadf82
7f7f7f
ffffff

Requirements
Must have
• coordinated feel per set, but each set can have its own look/font/etc

```html
<!DOCTYPE html>
<html lang="en">
<head>
<meta charset="utf-8">
<title>There's Snowplace Like Home</title>
<link rel="stylesheet" href="https://fonts.googleapis.com/css2?family=Montserrat:wght@800&family=Poppins:wght@300&family=Caveat+Brush&display=swap">
<style>
  :root {
    --paper: #ffffff;
    --ink: #555555;
    --holly-red: #ec1f27;
    --leaf-green: #7dc142;
    --snow-beige: #d9d0b6;
    --speckle: #e4e4e4;
  }
  html, body {
    margin: 0;
    padding: 0;
    width: 1200px;
    height: 2278px;
    overflow: hidden;
    background: var(--paper);
  }
  .canvas {
    position: relative;
    width: 1200px;
    height: 2278px;
    background: var(--paper);
  }
  .snowman-art {
    position: absolute;
    left: 0;
    top: 313px;
    width: 400px;
    height: 1055px;
    background: linear-gradient(180deg, #e8e0c8 0%, var(--snow-beige) 100%);
    border-radius: 0 200px 200px 0;
  }
  .phrase {
    position: absolute;
    right: 95px;
    margin: 0;
    line-height: 1;
    white-space: nowrap;
    text-align: right;
  }
  .phrase-theres {
    top: 236px;
    font-family: 'Montserrat', sans-serif;
    font-weight: 800;
    font-size: 128px;
    color: var(--ink);
    letter-spacing: 2px;
  }
  .phrase-snowplace {
    top: 360px;
    font-family: 'Caveat Brush', cursive;
    font-size: 178px;
    color: var(--leaf-green);
  }
  .phrase-like-home {
    top: 520px;
    font-family: 'Poppins', sans-serif;
    font-weight: 300;
    font-size: 130px;
    color: var(--ink);
  }
  .phrase-hearts {
    top: 700px;
    font-family: 'Caveat Brush', cursive;
    font-size: 160px;
    color: var(--holly-red);
    letter-spacing: 6px;
  }
  .phrase-come, .phrase-home {
    font-family: 'Montserrat', sans-serif;
    font-weight: 800;
    font-size: 226px;
    color: var(--ink);
  }
  .phrase-come { top: 890px; }
  .phrase-home { top: 1108px; }
  .phrase-for {
    top: 1330px;
    font-family: 'Montserrat', sans-serif;
    font-weight: 800;
    font-size: 128px;
    color: var(--ink);
  }
  .sprig-art {
    position: absolute;
    left: 437px;
    top: 1360px;
    width: 304px;
    height: 60px;
    background: linear-gradient(90deg, rgba(125,193,66,0.15), rgba(125,193,66,0.6));
    border-radius: 30px;
  }
  .rule {
    position: absolute;
    left: 95px;
    width: 1007px;
    height: 5px;
    background: var(--leaf-green);
  }
  .rule-top { top: 1512px; }
  .rule-bottom { top: 1825px; }
  .phrase-christmas {
    top: 1530px;
    right: auto;
    left: 76px;
    width: 1041px;
    text-align: center;
    font-family: 'Caveat Brush', cursive;
    font-size: 260px;
    color: var(--holly-red);
  }
  .snowfall-texture {
    position: absolute;
    left: 105px;
    top: 1860px;
    width: 1015px;
    height: 155px;
    background: linear-gradient(180deg, var(--speckle) 0%, rgba(228,228,228,0) 100%);
  }
</style>
</head>
<body>
  <main class="canvas">
    <div class="snowman-art" role="img" aria-label="Illustration of a smiling snowman with a red and green striped knit hat and a twig arm"></div>

    <h1 class="phrase phrase-theres">THERE’S</h1>
    <p class="phrase phrase-snowplace">snowplace</p>
    <p class="phrase phrase-like-home">like home</p>
    <p class="phrase phrase-hearts">HEARTS</p>
    <p class="phrase phrase-come">COME</p>
    <p class="phrase phrase-home">HOME</p>
    <div class="sprig-art" role="img" aria-label="Small green leafy sprig ornament"></div>
    <p class="phrase phrase-for">FOR</p>

    <div class="rule rule-top"></div>
    <p class="phrase phrase-christmas">Christmas</p>
    <div class="rule rule-bottom"></div>

    <div class="snowfall-texture" role="img" aria-label="Scattered dark snow-speck texture"></div>
  </main>
</body>
</html>
```